Brivane Redesign

We need a face lift for our website, www.brivane.com. We sell flooring and related products nationwide. We are interested in expanding the width of the website and introducing grays and black. We want the design to be both contemporary and user friendly.

```html
<!DOCTYPE html>
<html lang="en">
<head>
<meta charset="utf-8">
<title>Brivane – Flooring Online</title>
<link href="https://fonts.googleapis.com/css2?family=Ubuntu:wght@400;500;700&family=Open+Sans:wght@400;600;800&family=Alfa+Slab+One&display=swap" rel="stylesheet">
<style>
:root{
  --wood-dark:#4a2a14;
  --wood-mid:#8a5a30;
  --wood-light:#b07a45;
  --ink:#222;
  --ink-soft:#666;
  --panel:#fff;
  --bar-dark:#3a3a3a;
  --bar-mid:#555;
  --red:#c8202a;
  --red-dark:#9e151d;
  --nav-bg:#e9e9e9;
  --nav-line:#bcbcbc;
}
*{box-sizing:border-box;margin:0;padding:0}
html,body{width:859px;height:1200px;overflow:hidden}
body{
  position:relative;
  font-family:"Open Sans",Arial,sans-serif;
  color:var(--ink);
  background:
    repeating-linear-gradient(90deg,rgba(0,0,0,.10) 0 2px,transparent 2px 70px),
    linear-gradient(180deg,var(--wood-dark) 0%,var(--wood-mid) 45%,var(--wood-light) 70%,var(--wood-mid) 100%);
}
.abs{position:absolute}

/* top bar */
.utility{left:72px;top:18px;display:flex;gap:14px;color:#fff;font:500 11px "Ubuntu",sans-serif;align-items:center}
.utility span{display:flex;align-items:center;gap:5px}
.utility svg{width:18px;height:18px}
.hotline{right:68px;top:12px;color:#fff;font:700 26px "Ubuntu",sans-serif;letter-spacing:.5px}

/* header */
.header{left:67px;top:51px;width:725px;height:67px;background:var(--panel)}
.brand{left:12px;top:18px;font:700 26px "Ubuntu",sans-serif;color:var(--red);display:flex;align-items:center;gap:6px}
.brand i{display:block;width:16px;height:16px;background:var(--red)}
.search{left:328px;top:24px;width:236px;height:20px;border:1px solid #bbb;background:linear-gradient(#eee,#fafafa)}
.search b{position:absolute;right:2px;top:2px;width:15px;height:14px;background:#333}
.search svg{position:absolute;right:4px;top:3px}
.social{left:584px;top:21px;display:flex;gap:3px}
.social i{display:block;width:23px;height:23px;border-radius:3px;background:#8a4a1e}

/* nav */
.nav{left:67px;top:125px;width:725px;height:34px;background:linear-gradient(#f7f7f7,var(--nav-bg));display:flex}
.nav a{font:500 10px "Ubuntu",sans-serif;color:#333;text-decoration:none;border-right:1px solid var(--nav-line);display:flex;align-items:center;justify-content:center;padding:0 8px;height:100%}
.nav a:last-child{border:0}

/* hero */
.hero{left:67px;top:166px;width:725px;height:290px;background:linear-gradient(120deg,#b5703a 0%,#d39a62 40%,#a35f2c 75%,#7a4520 100%);overflow:hidden}
.hero-kicker{left:90px;top:66px;font:500 33px "Ubuntu",sans-serif;color:#fff;text-shadow:0 2px 3px rgba(0,0,0,.4)}
.hero-title{left:88px;top:88px;font:800 108px/1 "Open Sans",sans-serif;color:#fff;letter-spacing:-4px;text-shadow:0 3px 5px rgba(0,0,0,.35)}
.btn{background:var(--red);color:#fff;font:500 13px "Ubuntu",sans-serif;border-radius:3px;display:flex;align-items:center;justify-content:center;gap:6px}
.hero-btn{left:90px;top:216px;width:108px;height:28px}
.promo{left:583px;top:18px;width:122px;height:142px;background:rgba(40,25,15,.85);border-radius:6px;color:#eee;font:400 8.6px/13px Arial,sans-serif;padding:14px 10px}
.promo u{color:#fff}
.promo .btn{margin-top:8px;height:28px;font-size:9px;line-height:10px;text-align:center}
.hero-brand{right:22px;bottom:22px;font:700 20px "Ubuntu",sans-serif;color:var(--red-dark)}

/* sidebar */
.sidebar{left:67px;top:475px;width:148px}
.side-group{margin-bottom:7px}
.side-group h3{background:var(--panel);height:34px;font:400 14.5px "Ubuntu",sans-serif;color:#444;padding:8px 12px}
.side-group li{list-style:none;height:17.5px;font:500 9px/17.5px "Ubuntu",sans-serif;color:#fff;padding-left:13px}
.side-group li:nth-child(odd){background:var(--bar-dark)}
.side-group li:nth-child(even){background:var(--bar-mid)}

/* products */
.product{top:475px;width:178px;height:295px;background:var(--panel)}
.product .shot{height:233px}
.price{left:-8px;top:20px;height:30px;padding:0 20px 0 14px;background:linear-gradient(90deg,#2a2a2a,#c8202a);color:#fff;font:700 17px/30px "Ubuntu",sans-serif;clip-path:polygon(0 0,88% 0,100% 50%,88% 100%,0 100%)}
.price small{font:400 9px "Ubuntu",sans-serif}
.product .name{padding:8px 14px;font:500 14px/15px "Ubuntu",sans-serif;color:#333}
.product .name span{display:block;font-weight:400;font-size:12.5px;color:#888;line-height:13px}

/* free samples */
.samples{left:232px;top:787px;width:561px;height:93px;background:var(--panel)}
.samples .free{left:14px;top:10px;font:32px/1 "Alfa Slab One",serif;color:var(--red)}
.samples .word{left:14px;top:42px;font:400 39px/1 "Ubuntu",sans-serif;color:#333}
.samples .banner{left:254px;top:8px;width:294px;height:78px;background:linear-gradient(90deg,#6b3a1c,#b6804e 50%,#5a2e14)}
.samples .banner p{position:absolute;left:10px;top:14px;width:274px;height:50px;background:rgba(0,0,0,.55);color:#fff;font:500 21px/50px "Ubuntu",sans-serif;text-align:center}

/* newsletter */
.newsletter{left:232px;top:896px;width:561px;height:49px;background:var(--panel)}
.newsletter h4{position:absolute;left:69px;top:14px;font:500 16px "Ubuntu",sans-serif;color:var(--red)}
.newsletter .field{position:absolute;left:230px;top:16px;width:189px;height:20px;border:1px solid #aaa;font:400 8.5px/18px Arial,sans-serif;color:#555;padding-left:6px}
.newsletter .send{position:absolute;left:425px;top:16px;width:52px;height:20px;background:#222;color:#fff;font:500 11px/20px "Ubuntu",sans-serif;text-align:center}

/* footer */
.footer{left:67px;top:967px;width:725px;height:200px;background:var(--panel)}
.badge{background:#d4d4d4;border-radius:3px}
.card{width:27px;height:17px;border-radius:2px}
.cards{left:200px;top:32px;display:flex;gap:4px}
.links{left:140px;top:67px;width:290px;text-align:center;font:600 9.5px/13px "Open Sans",sans-serif;color:#222}
.copyright{left:140px;top:101px;width:290px;text-align:center;font:400 8.5px/14px Arial,sans-serif;color:#333}
.copyright u{margin:0 3px}
.footer-brand{left:500px;top:40px;font:700 26px "Ubuntu",sans-serif;color:var(--red);display:flex;align-items:center;gap:6px}
.footer-brand i{display:block;width:16px;height:16px;background:var(--red)}
.support{left:497px;top:92px;font:400 9.6px/12.4px Arial,sans-serif;color:#222}
.support p+p{margin-top:12px}
</style>
</head>
<body>

<div class="abs utility">
  <span><svg viewBox="0 0 18 18"><rect x="1" y="3" width="16" height="13" rx="1" fill="#e9c25a"/><rect x="3" y="6" width="12" height="2" fill="#fff"/></svg>Order Tracking</span>
  <span><svg viewBox="0 0 18 18"><rect x="1" y="1" width="16" height="16" rx="2" fill="#f08a1c"/><circle cx="9" cy="7" r="3" fill="#fff"/><rect x="4" y="11" width="10" height="3" fill="#fff"/></svg>My Account</span>
  <span><svg viewBox="0 0 18 18"><rect x="1" y="1" width="16" height="16" rx="2" fill="#ddd"/><path d="M4 6h10l-1 5H5z" fill="#777"/><circle cx="6" cy="13" r="1.2" fill="#777"/><circle cx="12" cy="13" r="1.2" fill="#777"/></svg>0 Product(s) in cart</span>
</div>
<div class="abs hotline">1-800-555-0142</div>

<header class="abs header">
  <div class="abs brand"><i></i>Brivane</div>
  <div class="abs search"><b></b><svg width="10" height="10" viewBox="0 0 10 10"><circle cx="4" cy="4" r="3" stroke="#fff" stroke-width="1.4" fill="none"/><path d="M6 6l3 3" stroke="#fff" stroke-width="1.6"/></svg></div>
  <div class="abs social"><i></i><i></i><i></i><i></i><i></i></div>
</header>

<nav class="abs nav">
  <a style="width:68px">LAMINATE</a><a style="width:73px">HARDWOOD</a><a style="width:70px">AREA RUGS</a><a style="width:62px">BAMBOO</a><a style="width:47px">CORK</a><a style="width:53px">VINYL</a><a style="width:83px">CARPET TILE</a><a style="width:46px">TILE</a><a style="width:60px">CLOCKS</a><a style="width:47px">BATH</a><a style="width:116px">CLEARANCE</a>
</nav>

<section class="abs hero" role="img" aria-label="Close-up photo of stacked hardwood floor planks with a free shipping stamp">
  <div class="abs hero-kicker">FREE SHIPPING</div>
  <div class="abs hero-title">sale</div>
  <div class="abs btn hero-btn">Read more <svg width="14" height="10" viewBox="0 0 14 10"><path d="M0 3h8V0l6 5-6 5V7H0z" fill="#fff"/></svg></div>
  <div class="abs promo">
    Offering discount prices on <u>laminate</u>, <u>hardwood</u>, <u>cork</u>, <u>bamboo</u>, <u>vinyl</u> and <u>area rugs</u> from the brands you know and trust.
    <div class="btn">CURRENT<br>PROMOTIONS</div>
  </div>
  <div class="abs hero-brand">Brivane</div>
</section>

<aside class="abs sidebar">
  <div class="side-group"><h3>Shop By Brand</h3><ul><li>Laminate</li><li>Hardwood</li><li>Bamboo</li><li>Cork</li><li>Vinyl</li><li>Carpet Tile</li><li>Tile</li></ul></div>
  <div class="side-group"><h3>Home Decor</h3><ul><li>Area Rugs</li><li>Bath</li><li>Clocks</li></ul></div>
  <div class="side-group"><h3>Accessories</h3><ul><li>Underlayment</li><li>Trim &amp; Molding</li><li>Floor Cleaner</li><li>Installation Tools</li></ul></div>
  <div class="side-group"><h3>Flooring Facts</h3><ul><li>Laminate</li><li>Hardwood</li><li>Cork</li><li>Area Rugs</li></ul></div>
</aside>

<article class="abs product" style="left:231px">
  <div class="shot" role="img" aria-label="Room with light laminate floor and open doorway" style="background:linear-gradient(160deg,#e8d6b8,#c58a4c 60%,#9a5a28)"></div>
  <div class="abs price">2.49 <small>sq.ft.</small></div>
  <div class="name">Hallmere<span>Coastal Haven</span><span>12mm Laminate</span></div>
</article>
<article class="abs product" style="left:422px">
  <div class="shot" role="img" aria-label="Hallway with grey vinyl tile floor and a table lamp" style="background:linear-gradient(170deg,#d8c9b5,#9a8a7a 55%,#6f6258)"></div>
  <div class="abs price">3.79 <small>sq.ft.</small></div>
  <div class="name">Dunmore<span>Stonecraft</span><span>Luxury Vinyl Tile</span></div>
</article>
<article class="abs product" style="left:614px">
  <div class="shot" role="img" aria-label="Living room with rustic acacia hardwood floor by a fireplace" style="background:linear-gradient(170deg,#8aa06a,#6b4a2e 45%,#9a5e2a)"></div>
  <div class="abs price">4.99 <small>sq.ft.</small></div>
  <div class="name">Hallmere<span>Timber Ridge</span><span>Acacia Hardwood</span></div>
</article>

<section class="abs samples">
  <div class="abs free">FREE</div>
  <div class="abs word">SAMPLES</div>
  <div class="abs banner" role="img" aria-label="Row of wood floor sample swatches"><p>No credit card required</p></div>
</section>

<section class="abs newsletter">
  <h4>Join our Newsletter</h4>
  <div class="field">Please your enter email id</div>
  <div class="send">SEND</div>
</section>

<footer class="abs footer">
  <div class="abs badge" style="left:26px;top:33px;width:50px;height:28px"></div>
  <div class="abs badge" style="left:26px;top:80px;width:80px;height:22px"></div>
  <div class="abs badge" style="left:24px;top:140px;width:38px;height:34px;border-radius:50%"></div>
  <div class="abs badge" style="left:80px;top:140px;width:34px;height:34px;border-radius:50%;background:#e6d27a"></div>
  <div class="abs badge" style="left:130px;top:149px;width:44px;height:18px"></div>
  <div class="abs badge" style="left:192px;top:147px;width:46px;height:26px;background:#c8d4e4"></div>
  <div class="abs badge" style="left:258px;top:144px;width:54px;height:32px"></div>
  <div class="abs cards">
    <div class="card badge"></div><div class="card badge"></div><div class="card badge"></div><div class="card badge"></div><div class="card badge"></div><div class="card badge"></div>
  </div>
  <div class="abs links">about us | careers | consumer reviews | contact us | faq<br>ordering | pricing | privacy policy | return policy | shipping | sitemap</div>
  <div class="abs copyright">©1999-2014 Northway Home Goods, Inc. All rights reserved.<br><u>Faq</u><u>Privacy</u><u>Terms &amp; Conditions</u></div>
  <div class="abs footer-brand"><i></i>Brivane</div>
  <div class="abs support">
    <p>U.S residents call toll free: 1-800-555-0142.<br>Non-U.S. residents call: 1-815-555-0187.</p>
    <p>Our live support staff is available between:<br>8:00 a.m.- 5:00 p.m. CST, Monday thru Friday<br>9:00 a.m.- 5:00 p.m. CST, Saturday</p>
  </div>
</footer>

</body>
</html>
```